Stationary, Envelopes, Business Cards, Brouchures, Etc Ventisca Home Health
Pediatric Home Health
Stationary, Envelopes, Business Cards, Brouchures, Etc Ventisca Home Health -
Creative Brief
Bright & Fun-filled
Tobias Quillmore
Administrator
4817 Linwood Rd. Suite 318 Alderwick, Texas 78011 5400 Harlan Pruett Brennan Falls, Texas 79077
Alderwick: 210-555-0147
Brennan Falls: 915-555-0182
Mobile: 210-555-0163
Fax: 1-866-555-0129
tobias@myventisca.example
www.myventisca.example
Please keep in mind that we have two locations and would like to include both addresses and phone numbers.
Private Duty Nursing Speech Therapy Physical Therapy Occupational Therapy

```html
<!DOCTYPE html>
<html lang="en">
<head>
<meta charset="utf-8">
<title>Ventisca Home Health – Stationery</title>
<link rel="stylesheet" href="https://fonts.googleapis.com/css2?family=Open+Sans:wght@400;600;700&display=swap">
<style>
:root{
  --orange:#f7841f;
  --orange-deep:#ee6a10;
  --orange-light:#fbb24a;
  --brand:#3c63a9;
  --ink:#4a4a4a;
  --muted:#8a8a8a;
  --line:#b9b9b9;
  --swoosh-grey:#cfcfcf;
  --paper:#ffffff;
  --bg:#ffffff;
}
*{box-sizing:border-box;margin:0;padding:0}
html,body{width:1200px;height:590px;overflow:hidden;background:var(--bg);font-family:"Open Sans",Arial,sans-serif;color:var(--ink)}
.canvas{position:relative;width:1200px;height:590px}
.sheet{position:absolute;background:var(--paper);box-shadow:0 0 3px rgba(0,0,0,.25);overflow:hidden}
.fax{left:12px;top:12px;width:372px;height:516px}
.letter{left:408px;top:12px;width:372px;height:516px}
.card{position:absolute;box-shadow:0 0 3px rgba(0,0,0,.25);overflow:hidden;background:var(--paper)}
.card-front{left:828px;top:43px;width:348px;height:120px}
.card-back{left:828px;top:180px;width:348px;height:120px;background:linear-gradient(90deg,var(--orange-light),var(--orange) 55%,var(--orange-deep))}
.envelope{position:absolute;left:828px;top:324px;width:348px;height:192px;background:var(--paper);box-shadow:0 0 3px rgba(0,0,0,.25);overflow:hidden}
.swoosh{position:absolute;left:0;bottom:0;width:100%}
.brand{position:absolute;display:flex;align-items:center;gap:5px}
.brand-dot{width:14px;height:14px;border-radius:50%;background:var(--orange)}
.brand-name{font-weight:700;color:var(--brand);font-size:10px;line-height:1.1;width:70px}
.contact{position:absolute;font-size:4.6px;line-height:1.45;color:var(--muted);text-align:left;white-space:nowrap}
.watermark{position:absolute;border-radius:50%;background:radial-gradient(circle,rgba(247,132,31,.16),rgba(247,132,31,0) 70%)}
.fax-title{position:absolute;right:22px;top:62px;font-size:15px;font-weight:700;color:#222;letter-spacing:.5px}
.fax-table{position:absolute;left:22px;top:86px;width:328px;border-collapse:collapse;font-size:7px}
.fax-table td{border:1px solid var(--line);height:19px;padding:0 4px;color:#444}
.fax-table td.label{width:40px}
.checks{position:absolute;left:22px;top:172px;width:328px;display:flex;justify-content:space-between;font-size:6px;color:#444}
.checks span::before{content:"";display:inline-block;width:5px;height:5px;border:1px solid #666;margin-right:2px;vertical-align:-1px}
.letter-body{position:absolute;left:30px;top:78px;width:312px;font-size:5.2px;line-height:1.55;color:#555}
.letter-body p{margin-bottom:6px}
.signature{width:50px;height:12px;border-bottom:1px solid #777;margin:4px 0 3px}
.seal{position:absolute;left:118px;top:360px;width:26px;height:26px;border-radius:50%;border:2px solid #7a74a8;opacity:.7}
.card-name{position:absolute;font-size:7px;font-weight:700;color:var(--orange-deep)}
.card-role{position:absolute;font-size:5px;color:var(--muted)}
.card-back .brand-name{color:#fff;font-size:13px;width:110px}
.card-back .brand-dot{background:#fff;width:18px;height:18px}
</style>
</head>
<body>
<div class="canvas">

  <section class="sheet fax">
    <div class="brand" style="left:22px;top:18px"><span class="brand-dot"></span><span class="brand-name">Ventisca Home Health</span></div>
    <div class="contact" style="left:250px;top:16px">4817 Linwood Rd. Suite 318<br>Alderwick, Texas 78011<br>5400 Harlan Pruett<br>Brennan Falls, Texas 79077<br>AW: 210-555-0147 · BF: 915-555-0182</div>
    <div class="fax-title">FAX</div>
    <table class="fax-table">
      <tr><td class="label">To:</td><td></td><td class="label">From:</td><td></td></tr>
      <tr><td class="label">Fax:</td><td></td><td class="label">Pages:</td><td></td></tr>
      <tr><td class="label">Phone:</td><td></td><td class="label">Date:</td><td></td></tr>
      <tr><td class="label">Re:</td><td></td><td class="label">CC:</td><td></td></tr>
    </table>
    <div class="checks"><span>Urgent</span><span>For Review</span><span>Please Comment</span><span>Please Reply</span><span>Please Recycle</span></div>
    <div class="watermark" role="img" aria-label="Faint brand watermark" style="left:150px;top:300px;width:160px;height:130px"></div>
    <svg class="swoosh" viewBox="0 0 372 110" height="110" preserveAspectRatio="none">
      <path d="M0 40 C120 95 250 95 372 20 L372 110 L0 110Z" fill="var(--orange)"/>
      <path d="M0 62 C130 105 260 90 372 48 L372 110 L0 110Z" fill="var(--orange-deep)"/>
      <path d="M0 30 C120 85 250 85 372 10" fill="none" stroke="var(--swoosh-grey)" stroke-width="3"/>
    </svg>
    <div class="contact" style="left:22px;bottom:10px;color:#fff">www.myventisca.example</div>
  </section>

  <section class="sheet letter">
    <div class="brand" style="left:30px;top:18px"><span class="brand-dot"></span><span class="brand-name">Ventisca Home Health</span></div>
    <div class="contact" style="left:250px;top:16px">4817 Linwood Rd. Suite 318<br>Alderwick, Texas 78011<br>5400 Harlan Pruett<br>Brennan Falls, Texas 79077<br>AW: 210-555-0147 · BF: 915-555-0182</div>
    <div class="letter-body">
      <p>Someone Somebody<br>12 Sample Lane<br>Corvale Country</p>
      <p>Dear Someone Somebody,</p>
      <p>Thank you for trusting our team with the care of your child. Our nurses and therapists visit families across two regions and bring patient, playful support to every home we serve each week.</p>
      <p>Each care plan is built with parents, doctors and schools so that progress is steady and easy to follow. We share notes after every visit and keep schedules flexible for busy households.</p>
      <p>Our services include private duty nursing, speech therapy, physical therapy and occupational therapy, all delivered by licensed staff who know how to make hard work feel like play.</p>
      <p>Please reach out to either office with questions at any time. We look forward to working with you and your family.</p>
      <p>Yours Sincerely,</p>
      <div class="signature"></div>
      <p>Tobias Quillmore</p>
    </div>
    <div class="seal" role="img" aria-label="Certificate stamp"></div>
    <div class="watermark" role="img" aria-label="Faint brand watermark" style="left:160px;top:300px;width:160px;height:130px"></div>
    <svg class="swoosh" viewBox="0 0 372 110" height="110" preserveAspectRatio="none">
      <path d="M0 40 C120 95 250 95 372 20 L372 110 L0 110Z" fill="var(--orange)"/>
      <path d="M0 62 C130 105 260 90 372 48 L372 110 L0 110Z" fill="var(--orange-deep)"/>
      <path d="M0 30 C120 85 250 85 372 10" fill="none" stroke="var(--swoosh-grey)" stroke-width="3"/>
    </svg>
    <div class="contact" style="left:30px;bottom:10px;color:#fff">www.myventisca.example</div>
  </section>

  <section class="card card-front">
    <svg style="position:absolute;right:0;top:0;height:120px;width:120px" viewBox="0 0 120 120" preserveAspectRatio="none">
      <path d="M120 0 L60 0 C20 40 20 80 60 120 L120 120Z" fill="var(--orange)"/>
      <path d="M120 0 L85 0 C55 40 55 80 85 120 L120 120Z" fill="var(--orange-deep)"/>
      <path d="M50 0 C12 40 12 80 50 120" fill="none" stroke="var(--swoosh-grey)" stroke-width="2.5"/>
    </svg>
    <div class="brand" style="left:14px;top:14px"><span class="brand-dot"></span><span class="brand-name" style="font-size:9px">Ventisca Home Health</span></div>
    <div class="card-name" style="left:14px;top:50px">Tobias Quillmore</div>
    <div class="card-role" style="left:14px;top:60px">Administrator</div>
    <div class="contact" style="left:14px;top:72px;color:#666">Alderwick: 210-555-0147 · Brennan Falls: 915-555-0182<br>Mobile: 210-555-0163 · Fax: 1-866-555-0129<br>tobias@myventisca.example<br>www.myventisca.example</div>
  </section>

  <section class="card card-back">
    <div class="brand" style="left:110px;top:44px"><span class="brand-dot"></span><span class="brand-name">Ventisca Home Health</span></div>
  </section>

  <section class="envelope">
    <div class="brand" style="left:14px;top:14px"><span class="brand-dot"></span><span class="brand-name" style="font-size:9px">Ventisca Home Health</span></div>
    <div class="contact" style="left:14px;top:40px">4817 Linwood Rd. Suite 318<br>Alderwick, Texas 78011<br>5400 Harlan Pruett<br>Brennan Falls, Texas 79077</div>
    <div class="watermark" role="img" aria-label="Faint brand watermark" style="left:150px;top:40px;width:130px;height:110px"></div>
    <svg class="swoosh" viewBox="0 0 348 60" height="60" preserveAspectRatio="none">
      <path d="M0 22 C110 55 240 55 348 10 L348 60 L0 60Z" fill="var(--orange)"/>
      <path d="M0 36 C120 60 240 55 348 28 L348 60 L0 60Z" fill="var(--orange-deep)"/>
      <path d="M0 14 C110 48 240 48 348 3" fill="none" stroke="var(--swoosh-grey)" stroke-width="2"/>
    </svg>
  </section>

</div>
</body>
</html>
```